Lawn care & general maintenance

I need a business card desisign for a new business in north bay called The Hedge Buddy i offer services like lawn care, snow removal, and general maintenance such as dry walling painting, brush removal, and other little maintenance work.

The font must be like the font on my work hate

Industry/Entity Type

Business

Contact Information for Business Card

Derek Ossington, Company name: The Hedge Buddy

Logo Text

The Hedge Buddy- in jetson print

Logo styles of interest
Pictorial/Combination Logo
Requirements
Must have
• Slogan: We mow down the toughest jobs, just ask!

```html
<!DOCTYPE html>
<html lang="en">
<head>
<meta charset="utf-8">
<title>The Hedge Buddy — Business Card</title>
<link rel="stylesheet" href="https://fonts.googleapis.com/css2?family=Oswald:wght@300;400;500;700&display=swap">
<style>
  :root {
    --page-bg: #e9e6e2;
    --card-brown: #574741;
    --card-white: #ffffff;
    --accent-orange: #f7941d;
    --text-light: #ffffff;
    --text-dark: #4a3a34;
  }
  html, body {
    margin: 0;
    width: 1200px;
    height: 900px;
    overflow: hidden;
    background: var(--page-bg);
    font-family: "Oswald", "Arial Narrow", sans-serif;
  }
  .business-card {
    position: absolute;
    left: 100px;
    top: 164px;
    width: 1000px;
    height: 572px;
    background: var(--card-brown);
    overflow: hidden;
    box-shadow: 0 10px 30px rgba(0,0,0,0.25);
  }
  .brand-band {
    position: absolute;
    left: 0; top: 0;
    width: 100%;
    height: 150px;
    background: var(--card-white);
  }
  .brand-lockup {
    position: absolute;
    left: 70px;
    top: 78px;
    display: flex;
    align-items: center;
    gap: 14px;
  }
  .brand-mark {
    width: 40px;
    height: 40px;
    background: var(--accent-orange);
  }
  .brand-divider {
    width: 2px;
    height: 52px;
    background: var(--text-dark);
  }
  .brand-name {
    font-weight: 700;
    font-size: 38px;
    line-height: 1;
    color: var(--text-dark);
  }
  .tool-art {
    position: absolute;
    right: 0;
    top: 40px;
    width: 200px;
    height: 532px;
  }
  .owner-name {
    position: absolute;
    left: 88px;
    top: 168px;
    margin: 0;
    font-size: 92px;
    line-height: 1.05;
    color: var(--text-light);
    font-weight: 300;
    white-space: nowrap;
  }
  .owner-name .surname { font-weight: 500; }
  .name-rule {
    position: absolute;
    left: 92px;
    top: 286px;
    width: 600px;
    border-top: 6px dashed var(--accent-orange);
  }
  .service-list {
    position: absolute;
    left: 98px;
    top: 298px;
    margin: 0;
    font-size: 22px;
    font-weight: 300;
    color: var(--text-light);
    letter-spacing: 0.3px;
  }
  .service-list strong { font-weight: 700; }
  .maintenance-note {
    position: absolute;
    left: 100px;
    top: 400px;
    margin: 0;
    font-size: 24px;
    font-weight: 400;
    color: var(--text-light);
  }
  .slogan {
    position: absolute;
    left: 100px;
    top: 436px;
    margin: 0;
    font-size: 32px;
    font-weight: 700;
    color: var(--text-light);
  }
  .slogan-swoosh {
    position: absolute;
    left: 300px;
    top: 478px;
    width: 300px;
    height: 24px;
  }
</style>
</head>
<body>
  <section class="business-card">
    <header class="brand-band">
      <div class="brand-lockup">
        <span class="brand-mark"></span>
        <span class="brand-divider"></span>
        <span class="brand-name">The Hedge Buddy</span>
      </div>
    </header>

    <svg class="tool-art" viewBox="0 0 200 532" role="img" aria-label="Orange illustration of a trowel, wrench and paint roller">
      <polygon points="110,0 200,0 200,532 150,532 60,440 110,300 70,180" fill="var(--accent-orange)" opacity="0.9"/>
    </svg>

    <h1 class="owner-name">Derek <span class="surname">Ossington</span></h1>
    <div class="name-rule"></div>
    <p class="service-list"><strong>lawn</strong> care, <strong>snow</strong> removal, <strong>drywall</strong> painting, <strong>brush</strong> removal.</p>

    <p class="maintenance-note">General Maintenance Work.</p>
    <p class="slogan">We mow down the toughest jobs, just ask!</p>
    <svg class="slogan-swoosh" viewBox="0 0 300 24">
      <path d="M4 18 Q150 2 296 6" stroke="var(--accent-orange)" stroke-width="4" fill="none" stroke-linecap="round"/>
    </svg>
  </section>
</body>
</html>
```